Stationery Design Project

We need letterhead and business cards designed for our consulting firm. Color scheme, mostly deep blue (see logo). We are a commercial consulting work out firm, nationwide (large loans, $10MM and up). Visit our website for more info.
Updates

Project Deadline Extended
Reason: Meeting tomorrow morning to make final final decision. Would like this project to stay open to be able to provide feed back and receive final edits and approve. Thank you!!!

Target Market(s)

High end investors

Industry/Entity Type

Business

Requirements
Must have
• Letterhead must have the logo and the address

4817 Larkmoor Avenue, Suite 210, San Diego, CA 92107
Nice to have
• It would be nice to incorporate a watermark of all or some portion of the logo on the letterhead, or at least for the 2nd sheets.

Maybe our phone number: 858.555.0174
and/or webiste: www.tollandridgecap.example
Should not have
• Target users and audience of this will be men so, frilly or whimsical type designs are not preferred.

```html
<!DOCTYPE html>
<html lang="en">
<head>
<meta charset="utf-8">
<title>Tolland Ridge Capital – Stationery</title>
<link href="https://fonts.googleapis.com/css2?family=Open+Sans:wght@400;600;700&display=swap" rel="stylesheet">
<style>
  :root {
    --bg: #d9dadc;
    --paper: #ffffff;
    --brand-blue: #2a8fd0;
    --brand-blue-deep: #15638f;
    --brand-blue-light: #46a9e4;
    --ink-grey: #6f7377;
    --card-dark: #1f1f21;
    --card-dark-2: #323235;
    --white: #ffffff;
  }
  * { box-sizing: border-box; margin: 0; padding: 0; }
  html, body { width: 1200px; height: 948px; overflow: hidden; }
  body {
    background: var(--bg);
    font-family: "Open Sans", Arial, sans-serif;
    position: relative;
  }

  /* Letterhead */
  .letterhead {
    position: absolute; left: 56px; top: 70px;
    width: 560px; height: 792px;
    background: var(--paper);
    box-shadow: 0 4px 16px rgba(0,0,0,.18);
  }
  .letterhead__band {
    position: absolute; left: 0; top: 0;
    width: 396px; height: 84px;
    background: var(--brand-blue);
    color: var(--white);
    padding: 10px 0 0 22px;
  }
  .letterhead__firm { font-size: 11px; font-weight: 600; letter-spacing: .3px; }
  .letterhead__address { font-size: 8px; margin: 1px 0 6px; }
  .contact-line { display: flex; align-items: center; gap: 6px; font-size: 9px; line-height: 14px; }
  .contact-line svg { width: 9px; height: 9px; flex: none; }
  .letterhead__tab {
    position: absolute; right: 0; top: 12px;
    width: 32px; height: 72px;
    background: var(--brand-blue-light);
  }
  .letterhead__brand {
    position: absolute; left: 400px; top: 30px; width: 124px;
    display: flex; align-items: center; gap: 5px;
  }

  .brand-name {
    font-family: "Open Sans", Arial, sans-serif;
    font-weight: 600;
    color: var(--ink-grey);
    letter-spacing: .5px;
    text-transform: uppercase;
    line-height: 1.1;
  }
  .brand-mark { flex: none; background: var(--brand-blue); }

  /* Envelope */
  .envelope {
    position: absolute; left: 660px; top: 90px;
    width: 500px; height: 240px;
    background: var(--paper);
    box-shadow: 0 4px 16px rgba(0,0,0,.18);
  }
  .envelope__stripe {
    position: absolute; left: 0; top: 30px;
    width: 22px; height: 210px;
    background: var(--brand-blue);
  }
  .envelope__brand {
    position: absolute; right: 40px; top: 106px;
    display: flex; align-items: center; gap: 10px;
  }
  .envelope__brand .brand-name { font-size: 26px; }
  .envelope__brand .brand-mark { width: 18px; height: 18px; }

  /* Business cards */
  .card {
    position: absolute; top: 400px;
    width: 240px; height: 140px;
    border-radius: 5px; overflow: hidden;
    box-shadow: 0 4px 14px rgba(0,0,0,.25);
  }
  .card--front {
    left: 660px;
    background: linear-gradient(160deg, var(--card-dark-2), var(--card-dark));
  }
  .card--front .card__brand {
    position: absolute; left: 0; right: 0; top: 42px;
    display: flex; justify-content: center; align-items: center; gap: 7px;
  }
  .card--front .brand-name { color: #b9bcbf; font-size: 15px; }
  .card--front .brand-mark { width: 10px; height: 10px; }
  .card__wave-band {
    position: absolute; left: 0; right: 0; bottom: 0; height: 34px;
    background: linear-gradient(180deg, var(--brand-blue-deep), var(--brand-blue));
  }

  .card--back {
    left: 920px;
    background: linear-gradient(135deg, var(--brand-blue-deep), var(--brand-blue) 60%, var(--brand-blue-deep));
    color: var(--white);
  }
  .card__person { position: absolute; left: 16px; top: 16px; }
  .card__name { font-size: 12px; font-weight: 700; }
  .card__title { font-size: 6.5px; opacity: .85; }
  .card__contacts { position: absolute; left: 16px; top: 60px; }
  .card__contacts .contact-line { font-size: 7.5px; line-height: 16px; }
  .card__web {
    position: absolute; left: 0; right: 0; bottom: 0; height: 20px;
    background: var(--white); color: var(--brand-blue-deep);
    font-size: 8px; font-weight: 600; letter-spacing: .5px;
    display: flex; align-items: center; justify-content: center;
  }
</style>
</head>
<body>

<section class="letterhead" aria-label="Letterhead">
  <div class="letterhead__band">
    <p class="letterhead__firm">TOLLAND RIDGE CAPITAL</p>
    <p class="letterhead__address">4817 Larkmoor Avenue, Suite 210, San Diego, CA 92107</p>
    <p class="contact-line">
      <svg viewBox="0 0 10 10"><rect x="0.5" y="0.5" width="9" height="9" rx="2" fill="none" stroke="#fff"/><path d="M3 2.5h1.2l.6 1.5-.8.6a4 4 0 0 0 1.7 1.7l.6-.8 1.5.6V7.5A4.5 4.5 0 0 1 3 2.5z" fill="#fff"/></svg>
      (858) 555-0174
    </p>
    <p class="contact-line">
      <svg viewBox="0 0 10 10"><rect x="0.5" y="2" width="9" height="6" fill="none" stroke="#fff"/><path d="M.5 2l4.5 3.5L9.5 2" fill="none" stroke="#fff"/></svg>
      info@tollandridgecap.example
    </p>
    <p class="contact-line">
      <svg viewBox="0 0 10 10"><circle cx="5" cy="5" r="4.3" fill="none" stroke="#fff"/><path d="M.7 5h8.6M5 .7c-2.4 2.4-2.4 6.2 0 8.6M5 .7c2.4 2.4 2.4 6.2 0 8.6" fill="none" stroke="#fff" stroke-width=".7"/></svg>
      www.tollandridgecap.example
    </p>
  </div>
  <div class="letterhead__brand">
    <span class="brand-mark" style="width:8px;height:8px"></span>
    <span class="brand-name" style="font-size:11px">Tolland Ridge Capital</span>
  </div>
  <div class="letterhead__tab"></div>
</section>

<section class="envelope" aria-label="Envelope">
  <div class="envelope__stripe"></div>
  <div class="envelope__brand">
    <span class="brand-mark"></span>
    <span class="brand-name">Tolland Ridge Capital</span>
  </div>
</section>

<section class="card card--front" aria-label="Business card front">
  <div class="card__brand">
    <span class="brand-mark"></span>
    <span class="brand-name">Tolland Ridge Capital</span>
  </div>
  <div class="card__wave-band" role="img" aria-label="Blue wave graphic along the bottom edge"></div>
</section>

<section class="card card--back" aria-label="Business card back">
  <div class="card__person">
    <p class="card__name">Owen Hadley</p>
    <p class="card__title">Chief Executive Officer</p>
  </div>
  <div class="card__contacts">
    <p class="contact-line">
      <svg viewBox="0 0 10 10"><rect x="0.5" y="0.5" width="9" height="9" rx="2" fill="none" stroke="#fff"/><path d="M3 2.5h1.2l.6 1.5-.8.6a4 4 0 0 0 1.7 1.7l.6-.8 1.5.6V7.5A4.5 4.5 0 0 1 3 2.5z" fill="#fff"/></svg>
      (858) 555-0174
    </p>
    <p class="contact-line">
      <svg viewBox="0 0 10 10"><rect x="0.5" y="2" width="9" height="6" fill="none" stroke="#fff"/><path d="M.5 2l4.5 3.5L9.5 2" fill="none" stroke="#fff"/></svg>
      info@tollandridgecap.example
    </p>
  </div>
  <p class="card__web">www.tollandridgecap.example</p>
</section>

</body>
</html>
```